Website Design for Bright Hearth e-zine

Website design for e-zine Bright Hearth, providing news and articles for healthy, positive and active family life.

```html
<!DOCTYPE html>
<html lang="en">
<head>
<meta charset="utf-8">
<title>Bright Hearth — Family e-zine</title>
<link href="https://fonts.googleapis.com/css2?family=Questrial&family=Arimo:wght@400;700&display=swap" rel="stylesheet">
<style>
  :root{
    --dark:#333333;
    --green-bg:#c1f08a;
    --brand-green:#8ccb22;
    --white:#ffffff;
    --ink:#1e1e1e;
    --muted-line:#9fce6c;
    --tab1:#6cb51e;
    --tab2:#18b6cf;
    --tab3:#e2401a;
    --tab4:#f08c12;
    --photo-a:#6f8a3c;
    --photo-b:#b9876a;
    --overlay:rgba(40,30,25,.55);
    --footer-line:#111111;
  }
  *{box-sizing:border-box;margin:0;padding:0}
  html,body{width:926px;height:1200px;overflow:hidden}
  body{position:relative;background:var(--green-bg);font-family:"Arimo",Arial,sans-serif;color:var(--ink)}
  .abs{position:absolute}
  .header-band{left:0;top:0;width:926px;height:135px;background:var(--dark)}
  .logo{left:153px;top:18px;font-family:"Arimo",Arial,sans-serif;font-weight:700;font-size:31px;color:var(--brand-green);letter-spacing:-.5px}
  .nav{left:360px;top:16px;display:flex;height:40px;align-items:center}
  .nav a{color:var(--white);font-weight:700;font-size:13px;text-decoration:none;padding:0 18px;line-height:40px;border-right:1px solid #222;box-shadow:1px 0 0 #4a4a4a}
  .nav a:last-child{border:none;box-shadow:none}
  .nav a.current{color:var(--brand-green)}
  .slider-card{left:126px;top:74px;width:675px;height:324px;background:var(--white);border-radius:22px;box-shadow:0 8px 10px rgba(0,0,0,.18)}
  .tab{left:149px;width:66px;height:46px;background:#f3f3f3;border-bottom:1px solid #e2e2e2}
  .tab.active{background:#1a1a1a;border-radius:24px 0 0 24px}
  .tab span{position:absolute;left:5px;top:5px;width:36px;height:36px;border-radius:50%;color:var(--white);font-size:19px;text-align:center;line-height:36px;font-family:"Arimo",Arial,sans-serif}
  .slide-photo{left:215px;top:88px;width:573px;height:297px;background:linear-gradient(120deg,var(--photo-a),var(--photo-b) 55%,#7a5a48);border-radius:0 0 8px 0}
  .slide-caption{left:580px;top:88px;width:208px;height:297px;background:var(--overlay);color:var(--white);text-align:center}
  .slide-caption .close{position:absolute;right:12px;top:6px;font-size:16px}
  .slide-caption h2{margin-top:46px;font-size:32px;font-weight:700;letter-spacing:-.5px}
  .slide-caption .sub{font-size:9px;font-weight:700;margin-top:4px}
  .slide-caption p{font-size:9.5px;line-height:17px;margin:22px 14px 0}
  .btn{display:block;background:var(--white);color:var(--ink);font-size:10px;font-weight:700;text-align:center;line-height:27px;height:27px;box-shadow:0 1px 2px rgba(0,0,0,.15)}
  .slide-caption .btn{width:82px;margin:22px auto 0}
  .quote{left:0;width:926px;text-align:center;font-family:"Questrial",sans-serif;font-size:26px;color:#222}
  .news{left:139px;top:542px;width:149px;list-style:none}
  .news li{font-size:10px;height:27.6px;line-height:27px;border-bottom:1px solid var(--muted-line);box-shadow:0 1px 0 #d6f7b0}
  .news li:last-child{border:none;box-shadow:none}
  .welcome-title{left:331px;top:544px;font-family:"Questrial",sans-serif;font-size:16px}
  .welcome-img{left:332px;top:570px;width:207px;height:90px;background:linear-gradient(90deg,#f7f0ff,#fff4ea);border-radius:5px}
  .welcome-text{left:332px;top:666px;width:212px;font-size:9.5px;line-height:14.3px}
  .features{left:579px;top:546px;width:220px}
  .feature{position:relative;padding-left:21px;height:71px;border-bottom:1px solid var(--muted-line);box-shadow:0 1px 0 #d6f7b0;margin-bottom:3px}
  .feature:last-child{border:none;box-shadow:none}
  .feature svg{position:absolute;left:0;top:3px}
  .feature h3{font-family:"Questrial",sans-serif;font-weight:400;font-size:14.5px}
  .feature p{font-size:9.5px;line-height:14.3px;margin-top:3px}
  .banner{left:298px;top:791px;width:503px;height:63px;background:var(--white);text-align:center;font-family:"Arimo",Arial,sans-serif;font-weight:700;color:#000}
  .banner .b1{font-size:33px;line-height:36px;padding-top:2px;letter-spacing:-1px}
  .banner .b2{font-size:19px;line-height:20px}
  .footer-band{left:0;top:884px;width:926px;height:316px;background:var(--dark)}
  .f-title{color:var(--white);font-weight:700;font-size:15px}
  .social{left:137px;top:932px;width:152px;list-style:none}
  .social li{height:27.5px;line-height:24px;color:var(--white);font-size:10px;font-weight:700;border-bottom:1px solid #2a2a2a;box-shadow:0 1px 0 #3f3f3f;display:flex;align-items:center;gap:10px}
  .social li i{display:inline-block;width:12px;height:12px;background:#4fa3d9}
  .thanks-text{left:328px;top:932px;width:214px;color:var(--white);font-size:9.5px;font-weight:700;line-height:15px}
  .ad-box{left:578px;top:934px;width:207px;height:170px;background:var(--white)}
  .rule{left:93px;top:1127px;width:730px;height:3px;background:var(--footer-line)}
  .copyright{left:0;top:1156px;width:926px;text-align:center;color:var(--white);font-size:9px;font-weight:700}
  .copyright .g{color:var(--brand-green)}
  .copyright .o{color:var(--tab4)}
</style>
</head>
<body>
  <div class="abs header-band"></div>
  <div class="abs logo">Bright Hearth</div>
  <nav class="abs nav">
    <a class="current" href="#">About</a>
    <a href="#">Events</a>
    <a href="#">Our Programs</a>
    <a href="#">Playtime</a>
    <a href="#">Contact Us</a>
  </nav>

  <section class="abs slider-card"></section>
  <div class="abs tab active" style="top:88px"><span style="background:var(--tab1)">01</span></div>
  <div class="abs tab" style="top:137px"><span style="background:var(--tab2)">02</span></div>
  <div class="abs tab" style="top:186px"><span style="background:var(--tab3)">03</span></div>
  <div class="abs tab" style="top:235px;border:none"><span style="background:var(--tab4)">04</span></div>
  <div class="abs slide-photo" role="img" aria-label="Photo of a smiling family lying on green grass, heads together"></div>
  <div class="abs slide-caption">
    <span class="close">✕</span>
    <h2>Holidays</h2>
    <div class="sub">TIME FOR FAMILY HOLIDAYS</div>
    <p>These days, everyone seems so busy that it can be hard to find time for family activities.</p>
    <a class="btn" href="#">Read More</a>
  </div>

  <p class="abs quote" style="top:412px">The happiest moment of my life have been the few which</p>
  <p class="abs quote" style="top:477px">I have passed at home in the bosom of my family.</p>

  <ul class="abs news">
    <li>News1</li><li>News2</li><li>News3</li><li>News4</li><li>News5</li>
    <li>News6</li><li>News7</li><li>News8</li><li>News9</li>
  </ul>

  <h2 class="abs welcome-title">Welcome !</h2>
  <div class="abs welcome-img" role="img" aria-label="Colourful illustration of paper-cut family figures under stars"></div>
  <p class="abs welcome-text">'Family' In most societies it is the principal institution for the socialization of children. Extended from the human "family unit" by biological-cultural affinity, marriage are concepts of family that are physical and metaphorical.</p>
  <a class="abs btn" href="#" style="left:333px;top:754px;width:83px">Read More</a>

  <div class="abs features">
    <div class="feature">
      <svg width="12" height="12" viewBox="0 0 12 12"><circle cx="6" cy="6" r="6" fill="#5aa51a"/><path d="M5 3.5 7.5 6 5 8.5" stroke="#fff" stroke-width="1.6" fill="none"/></svg>
      <h3>Our Vision</h3>
      <p>Family is combination of culture and affection and its all about the how strong we are.</p>
    </div>
    <div class="feature">
      <svg width="12" height="12" viewBox="0 0 12 12"><circle cx="6" cy="6" r="6" fill="#5aa51a"/><path d="M5 3.5 7.5 6 5 8.5" stroke="#fff" stroke-width="1.6" fill="none"/></svg>
      <h3>Perfect Experience</h3>
      <p>Store up your family memories and earn a badge with Badges of Fun.</p>
    </div>
    <div class="feature">
      <svg width="12" height="12" viewBox="0 0 12 12"><circle cx="6" cy="6" r="6" fill="#5aa51a"/><path d="M5 3.5 7.5 6 5 8.5" stroke="#fff" stroke-width="1.6" fill="none"/></svg>
      <h3>Columnists</h3>
      <p>Different Coulmns and articles which are shown here. you can read from here.</p>
    </div>
  </div>
  <a class="abs btn" href="#" style="left:602px;top:754px;width:82px">Read More</a>

  <div class="abs banner"><div class="b1">Banner</div><div class="b2">728 x 90</div></div>

  <footer class="abs footer-band"></footer>
  <h3 class="abs f-title" style="left:137px;top:911px">Stay Connected</h3>
  <ul class="abs social">
    <li><i></i>Friend Circle</li>
    <li><i></i>Quick Posts</li>
    <li><i></i>Work Network</li>
  </ul>
  <h3 class="abs f-title" style="left:326px;top:911px">Thanks Giving</h3>
  <p class="abs thanks-text">Thanksgiving Day is a holiday celebrated primarily in the United States and Canada. Thanksgiving is celebrated each year on the second Monday of October in Canada and on &nbsp;the fourth Thursday of November in the United States</p>
  <a class="abs btn" href="#" style="left:325px;top:1023px;width:82px">Read More</a>
  <h3 class="abs f-title" style="left:580px;top:911px">Advertisment</h3>
  <div class="abs ad-box"></div>
  <div class="abs rule"></div>
  <p class="abs copyright"><span class="g">Bright</span><span class="o">Hearth</span> © 2011 Lantern webTeam By Lantern Studio</p>
</body>
</html>
```